Develop website for Cloud Security Startup

Looking for a logo that conveys the outsourced security and management of clients data, systems and development in Tessora, Kfn and Brintel with an emphasis on security and compliance

Target Market(s)

Companies looking for professional services IT firm

Coding

Coded - Design and coding required

Number of Pages Required

5+ page

Font styles to use
Sans Serif

Colors
0455a3
33a6d7

Requirements
Must have
• Landing Page
- Help me get started

Move to the cloud safely
- Benefits of Cloud

What we do
- Cloud Adoption
- Managed Services
- Optimise

Resources
- News
- Resources
- Events
- Webinars
- Not for profit
- Case Studies
- Support Button
- Incident Button

Company
- About Us
- Why Vorselith?
- Acreditations
- Halvendor Tessora Partner
- Net Promoter Score
- Careers
- Contact Us

Contact Us

```html
<!DOCTYPE html>
<html lang="en">
<head>
<meta charset="utf-8">
<title>Vorselith — Effective Technology Management</title>
<link href="https://fonts.googleapis.com/css2?family=Montserrat:wght@400;500;600;700&family=Open+Sans:wght@400;600&display=swap" rel="stylesheet">
<style>
:root{
  --brand-dark:#0455a3;
  --brand-deep:#0d4c93;
  --hero-top:#0b3f7e;
  --brand-light:#33a6d7;
  --footer-blue:#0d56a8;
  --ink:#1c2230;
  --muted:#555b66;
  --card-border:#d9eef8;
  --white:#ffffff;
}
*{box-sizing:border-box;margin:0;padding:0}
html,body{width:1200px;height:3285px;overflow:hidden;background:var(--white)}
body{font-family:"Open Sans",Arial,sans-serif;color:var(--ink)}
.page{position:relative;width:1200px;height:3285px;overflow:hidden}
.abs{position:absolute}
.heading-font{font-family:"Montserrat",Arial,sans-serif}

/* hero */
.hero-bg{position:absolute;left:0;top:0}
.brand{position:absolute;left:108px;top:60px;color:var(--white);font-family:"Montserrat",sans-serif}
.brand-mark{display:inline-block;width:26px;height:26px;border-radius:50%;background:var(--white);vertical-align:middle;margin-right:10px}
.brand-name{font-size:32px;font-weight:600;letter-spacing:1px;vertical-align:middle}
.brand-tag{display:block;font-size:10px;font-weight:600;letter-spacing:.3px;margin-top:4px}
.search{position:absolute;left:817px;top:36px;width:271px;height:48px;border:1.5px solid rgba(255,255,255,.85);border-radius:24px;color:var(--white);font-family:"Montserrat",sans-serif;font-size:13px;font-weight:500;padding:14px 0 0 17px}
.search svg{position:absolute;right:18px;top:17px}
.nav{position:absolute;top:121px;left:0;font-family:"Montserrat",sans-serif;font-size:13.5px;font-weight:600;color:var(--white)}
.nav span{position:absolute;white-space:nowrap}
.hero-art{position:absolute;left:497px;top:150px;width:703px;height:470px;background:radial-gradient(ellipse at 55% 45%,rgba(80,190,240,.55),rgba(30,110,190,.25) 55%,rgba(11,63,126,0) 75%)}
.hero-title{position:absolute;left:97px;top:330px;font-family:"Montserrat",sans-serif;font-size:57px;font-weight:600;color:var(--white);letter-spacing:.5px}
.hero-sub{position:absolute;left:97px;top:402px;font-family:"Montserrat",sans-serif;font-size:27px;font-weight:500;color:var(--white)}
.btn{position:absolute;display:flex;align-items:center;justify-content:center;font-family:"Montserrat",sans-serif;font-weight:600;color:var(--white);border-radius:34px}
.btn-start{left:96px;top:463px;width:250px;height:64px;background:var(--brand-light);font-size:16px}

/* section heads */
.section-title{position:absolute;left:0;width:1200px;text-align:center;font-family:"Montserrat",sans-serif;font-weight:600;font-size:34px;color:var(--brand-dark)}
.section-rule{position:absolute;left:573px;width:54px;height:3px;background:var(--brand-light)}
.section-lead{position:absolute;left:0;width:1200px;text-align:center;font-size:17px;color:var(--muted)}

/* service cards */
.service{position:absolute;top:1081px;width:315px;height:395px;border:3px solid var(--card-border);border-radius:16px;background:var(--white);text-align:center}
.service-icon{position:absolute;left:72px;top:30px}
.service h3{position:absolute;top:242px;left:0;width:100%;font-family:"Montserrat",sans-serif;font-weight:500;font-size:21px;color:var(--ink)}
.service p{position:absolute;top:284px;left:32px;right:32px;font-size:14px;line-height:25px;color:var(--muted)}

/* about */
.about-bg{position:absolute;left:0;top:1520px}
.about-photo{position:absolute;left:0;top:1610px;width:640px;height:541px;background:linear-gradient(90deg,rgba(10,60,120,.35),rgba(51,166,215,0))}
.about-title{position:absolute;left:625px;top:1732px;font-family:"Montserrat",sans-serif;font-weight:600;font-size:38px;color:var(--white)}
.about-rule{position:absolute;left:625px;top:1790px;width:60px;height:3px;background:var(--white)}
.about-text{position:absolute;left:625px;top:1818px;width:447px;font-size:14.5px;line-height:25.7px;color:var(--white);text-align:justify}
.btn-learn{left:625px;top:2026px;width:183px;height:60px;background:var(--brand-dark);font-size:16px}

/* blog */
.post{position:absolute;top:2336px;width:315px;height:432px;border:2px solid #e4e6ea;border-radius:12px;background:var(--white);overflow:hidden;text-align:center}
.post-photo{height:229px}
.photo-a{background:linear-gradient(160deg,#0b3f66,#1e86b8 55%,#0c3658)}
.photo-b{background:linear-gradient(180deg,#0b2642,#23649a 45%,#071a2e)}
.photo-c{background:linear-gradient(135deg,#0a2234,#1a5e86 60%,#0a2a40)}
.post-date{position:absolute;left:112px;top:184px;width:90px;height:90px;border-radius:50%;color:var(--white);font-family:"Montserrat",sans-serif;border:3px solid var(--white)}
.post-date b{display:block;font-size:23px;font-weight:600;margin-top:15px}
.post-date i{display:block;font-style:normal;font-size:15px;font-weight:500}
.date-dark{background:var(--brand-dark)}
.date-light{background:var(--brand-light)}
.post h3{position:absolute;top:291px;left:0;width:100%;font-family:"Montserrat",sans-serif;font-weight:600;font-size:18.5px;color:#2b2f36}
.post p{position:absolute;top:328px;left:24px;right:24px;font-family:Arial,sans-serif;font-size:13.5px;line-height:25px;color:var(--muted)}

/* footer */
.footer-bg{position:absolute;left:0;top:2800px}
.footer-brand{position:absolute;left:179px;top:3080px;color:var(--white);font-family:"Montserrat",sans-serif}
.footer-brand .brand-name{font-size:38px}
.footer-brand .brand-tag{font-size:12px}
.footer-head{position:absolute;top:2978px;font-family:"Montserrat",sans-serif;font-size:18px;font-weight:500;color:var(--white);letter-spacing:.5px}
.footer-menu{position:absolute;left:506px;top:3024px;list-style:none;font-family:"Montserrat",sans-serif;font-size:12.5px;color:var(--white);line-height:24.3px}
.contact-item{position:absolute;left:660px;color:var(--white);font-size:13.5px;line-height:20px}
.contact-item .dot{position:absolute;left:0;top:4px;width:26px;height:26px;border-radius:50%;background:var(--white);display:flex;align-items:center;justify-content:center}
.contact-item span{display:block;margin-left:37px}
.follow-text{position:absolute;left:900px;top:3030px;width:200px;color:var(--white);font-size:12.5px;line-height:20px}
.newsletter{position:absolute;left:900px;top:3077px;width:190px;height:37px;background:var(--white);border-radius:3px;font-size:12px;color:var(--ink);padding:10px 0 0 10px}
.newsletter svg{position:absolute;right:14px;top:11px}
.footer-rule{position:absolute;left:110px;top:3188px;width:980px;height:1px;background:rgba(255,255,255,.3)}
.copyright{position:absolute;left:0;top:3225px;width:1200px;text-align:center;color:var(--white);font-size:14px}
</style>
</head>
<body>
<div class="page">

  <!-- hero -->
  <svg class="hero-bg" width="1200" height="910" viewBox="0 0 1200 910" aria-hidden="true">
    <defs>
      <linearGradient id="heroGrad" x1="0" y1="0" x2="1" y2="1">
        <stop offset="0" stop-color="#0b3f7e"/>
        <stop offset="1" stop-color="#0a4a94"/>
      </linearGradient>
    </defs>
    <path d="M0 0H1200V578L306 900L0 648Z" fill="#33a6d7"/>
    <path d="M0 0H1200V580L306 884L0 628Z" fill="url(#heroGrad)"/>
  </svg>

  <div class="brand">
    <span class="brand-mark"></span><span class="brand-name">VORSELITH</span>
    <span class="brand-tag">EFFECTIVE TECHNOLOGY MANAGEMENT</span>
  </div>

  <div class="search">SEARCH
    <svg width="12" height="12" viewBox="0 0 12 12"><circle cx="5" cy="5" r="3.6" fill="none" stroke="#fff" stroke-width="1.8"/><line x1="7.7" y1="7.7" x2="11" y2="11" stroke="#fff" stroke-width="1.8"/></svg>
  </div>

  <nav class="nav">
    <span style="left:506px">HOME</span>
    <span style="left:597px">WHAT WE DO</span>
    <span style="left:743px">RESOURCES</span>
    <span style="left:876px">COMPANY</span>
    <span style="left:997px">CONTACT US</span>
  </nav>

  <div class="hero-art" role="img" aria-label="Isometric illustration of people working around a secured cloud with laptops, monitors and data panels"></div>

  <h1 class="hero-title">VORSELITH</h1>
  <p class="hero-sub">Effective Technology Management</p>
  <div class="btn btn-start">HELP ME GET STARTED</div>

  <!-- what we do -->
  <h2 class="section-title" style="top:940px">WHAT WE DO</h2>
  <div class="section-rule" style="top:994px"></div>
  <p class="section-lead" style="top:1014px">Lorem ipsum dolor sit amet, consectetur adipiscing elit, sed do eiusmod tempor</p>

  <div class="service" style="left:110px">
    <svg class="service-icon" width="165" height="165" viewBox="0 0 165 165" aria-hidden="true">
      <circle cx="82" cy="82" r="76" fill="none" stroke="#0455a3" stroke-width="14"/>
      <circle cx="82" cy="82" r="58" fill="#33a6d7" opacity=".12"/>
      <rect x="52" y="88" width="60" height="30" rx="3" fill="none" stroke="#33a6d7" stroke-width="3"/>
      <path d="M60 86a12 12 0 0 1 12-18a16 16 0 0 1 28 6a10 10 0 0 1 2 12Z" fill="none" stroke="#33a6d7" stroke-width="3"/>
      <path d="M76 100v-14m-5 5l5-5l5 5M88 86v14m-5-5l5 5l5-5" fill="none" stroke="#33a6d7" stroke-width="2.5"/>
    </svg>
    <h3>Cloud Adoption</h3>
    <p>Lorem ipsum dolor sit amet, conse ctetur adipiscing elit, sed do eiusmod labore et dolore magna</p>
  </div>

  <div class="service" style="left:443px">
    <svg class="service-icon" width="165" height="165" viewBox="0 0 165 165" aria-hidden="true">
      <circle cx="82" cy="82" r="76" fill="none" stroke="#0455a3" stroke-width="14"/>
      <circle cx="82" cy="82" r="58" fill="#33a6d7" opacity=".12"/>
      <rect x="50" y="52" width="30" height="16" fill="none" stroke="#33a6d7" stroke-width="3"/>
      <rect x="50" y="76" width="30" height="16" fill="none" stroke="#33a6d7" stroke-width="3"/>
      <rect x="50" y="100" width="30" height="16" fill="none" stroke="#33a6d7" stroke-width="3"/>
      <circle cx="102" cy="84" r="10" fill="none" stroke="#33a6d7" stroke-width="3"/>
      <circle cx="102" cy="84" r="3" fill="#33a6d7"/>
      <path d="M80 60h10v48h-10M90 84h2" fill="none" stroke="#33a6d7" stroke-width="2.5"/>
    </svg>
    <h3>Managed Services</h3>
    <p>Lorem ipsum dolor sit amet, conse ctetur adipiscing elit, sed do eiusmod labore et dolore magna</p>
  </div>

  <div class="service" style="left:775px">
    <svg class="service-icon" width="165" height="165" viewBox="0 0 165 165" aria-hidden="true">
      <circle cx="82" cy="82" r="76" fill="none" stroke="#0455a3" stroke-width="14"/>
      <circle cx="82" cy="82" r="58" fill="#33a6d7" opacity=".12"/>
      <circle cx="82" cy="82" r="34" fill="none" stroke="#33a6d7" stroke-width="3" stroke-dasharray="10 5"/>
      <circle cx="82" cy="82" r="22" fill="none" stroke="#33a6d7" stroke-width="3"/>
      <text x="82" y="92" text-anchor="middle" font-family="Montserrat,sans-serif" font-size="28" font-weight="600" fill="#33a6d7">$</text>
    </svg>
    <h3>Optimise</h3>
    <p>Lorem ipsum dolor sit amet, conse ctetur adipiscing elit, sed do eiusmod labore et dolore magna</p>
  </div>

  <!-- about -->
  <svg class="about-bg" width="1200" height="632" viewBox="0 0 1200 632" aria-hidden="true">
    <path d="M0 26L861 142L1200 10V44L861 172L0 38Z" fill="#0455a3"/>
    <path d="M0 38L861 172L1200 44V632H0Z" fill="#2c9fd6"/>
  </svg>
  <div class="about-photo" role="img" aria-label="Photo of a technician working in a server room, tinted blue"></div>

  <h2 class="about-title">ABOUT VORSELITH</h2>
  <div class="about-rule"></div>
  <p class="about-text">Lorem ipsum dolor sit amet, consectetur adipiscing elit, sed do eiusmod tempor incididunt ut labore et dolore magna aliqua. Ut enim ad minim veniam, quis nostrud exercitation ullamco laboris nisi ut aliquip ex ea commodo consequat.Duis aute irure dolor in reprehenderit in voluptate velit esse cillum dolore eu fugiat nulla pariatur. Excepteur sint occaecat cupidatat non proident, sunt in culpa qui officia deserunt mollit anim id est laborum</p>
  <div class="btn btn-learn">LEARN MORE</div>

  <!-- blog -->
  <h2 class="section-title" style="top:2200px">LATEST BLOG</h2>
  <div class="section-rule" style="top:2254px"></div>
  <p class="section-lead" style="top:2273px">Lorem ipsum dolor sit amet, consectetur adipiscing elit, sed do eiusmod tempor</p>

  <article class="post" style="left:110px">
    <div class="post-photo photo-a" role="img" aria-label="Digital security concept image with a glowing padlock interface"></div>
    <div class="post-date date-dark"><b>02</b><i>MAY</i></div>
    <h3>LOREM IPSUM DOLOR SIT</h3>
    <p>But I must explain to you how all this mistaken idea of denouncing pleasure and pain was born and I will give</p>
  </article>

  <article class="post" style="left:442px">
    <div class="post-photo photo-b" role="img" aria-label="Photo of two engineers viewed from behind at a wall of monitors"></div>
    <div class="post-date date-light"><b>02</b><i>MAY</i></div>
    <h3>LOREM IPSUM DOLOR SIT</h3>
    <p>But I must explain to you how all this mistaken idea of denouncing pleasure and pain was born and I will give</p>
  </article>

  <article class="post" style="left:774px">
    <div class="post-photo photo-c" role="img" aria-label="Photo of an engineer with a laptop in a data centre aisle"></div>
    <div class="post-date date-dark"><b>02</b><i>MAY</i></div>
    <h3>LOREM IPSUM DOLOR SIT</h3>
    <p>But I must explain to you how all this mistaken idea of denouncing pleasure and pain was born and I will give</p>
  </article>

  <!-- footer -->
  <svg class="footer-bg" width="1200" height="485" viewBox="0 0 1200 485" aria-hidden="true">
    <path d="M0 22L325 110L1200 38V485H0Z" fill="#33a6d7"/>
    <path d="M0 42L325 118L1200 56V485H0Z" fill="#0d56a8"/>
  </svg>

  <div class="footer-brand">
    <span class="brand-mark" style="width:30px;height:30px"></span><span class="brand-name">VORSELITH</span>
    <span class="brand-tag">EFFECTIVE TECHNOLOGY MANAGEMENT</span>
  </div>

  <h4 class="footer-head" style="left:506px">MENU</h4>
  <ul class="footer-menu">
    <li>HOME</li><li>WHAT WE DO</li><li>RESOURCES</li><li>COMPANY</li><li>CONTACT US</li>
  </ul>

  <h4 class="footer-head" style="left:663px">CONTACT</h4>
  <div class="contact-item" style="top:3028px">
    <div class="dot"><svg width="10" height="13" viewBox="0 0 10 13"><path d="M5 0a5 5 0 0 1 5 5c0 3-5 8-5 8S0 8 0 5a5 5 0 0 1 5-5Z" fill="#0d56a8"/><circle cx="5" cy="5" r="1.8" fill="#fff"/></svg></div>
    <span>1458 Dummy Text<br>lorem, CA 91710</span>
  </div>
  <div class="contact-item" style="top:3082px">
    <div class="dot"><svg width="12" height="9" viewBox="0 0 12 9"><rect width="12" height="9" rx="1" fill="#0d56a8"/><path d="M0 1l6 4l6-4" fill="none" stroke="#fff" stroke-width="1.2"/></svg></div>
    <span>E mail Us<br>info@company.com</span>
  </div>

  <h4 class="footer-head" style="left:902px">FOLLOW US</h4>
  <p class="follow-text">At vero eos et accusamus et iusto odio dignissimos</p>
  <div class="newsletter">Email :
    <svg width="14" height="14" viewBox="0 0 14 14"><path d="M1 7L13 1L10 13L7 8Z" fill="none" stroke="#0455a3" stroke-width="1.4"/><path d="M7 8L13 1" stroke="#0455a3" stroke-width="1.2"/></svg>
  </div>

  <div class="footer-rule"></div>
  <p class="copyright">Copyright © 2021 All Rights Reserved</p>
</div>
</body>
</html>
```